Bref créative
Modern Creative Stationary for Tech Start up!!!
TheByteDepot - Business cards - Letterheads - Email Signature -
Use same font as used in my logo
Smaller Text can be different- but in line with theme.
Professional
Pavel Orsk
Sales & Logistics
3rd Floor Birch Court
7X Fernhill Street
Harrow
London
HBX 8QW
0208 731 XXXX
07452168XXX
pavel@thebytedepotz.com
thebytedepotz.com
We want a double sided Business card that is elegant, modern, sleek and also creative. The logo should give you an idea of where we want to go in terms of theme.
Be creative, Be sexy and try your hardest as there is plenty more work to be done after this project.
This is our Logo.
We do not really like the shaded background. So it might be best to keep it flat black.
This is the white version of our Logo. It may be an idea to use this for the stationary.

```html
<!DOCTYPE html>
<html lang="en">
<head>
<meta charset="utf-8">
<title>TheByteDepot Stationery</title>
<link href="https://fonts.googleapis.com/css2?family=Exo+2:wght@400;600;800&display=swap" rel="stylesheet">
<style>
  :root {
    --bg: #2b2b2b;
    --paper: #ffffff;
    --ink: #1a1a1a;
    --muted: #777777;
    --black: #0d0d0d;
    --green: #8cc63f;
    --blue: #1f8fd6;
    --orange: #f58220;
    --grey: #9a9a9a;
  }
  * { box-sizing: border-box; margin: 0; padding: 0; }
  html, body { width: 1200px; height: 754px; overflow: hidden; }
  body {
    background: var(--bg);
    font-family: "Exo 2", sans-serif;
    color: var(--ink);
    position: relative;
  }
  .sheet {
    position: absolute;
    background: var(--paper);
    box-shadow: 0 6px 18px rgba(0,0,0,.45);
  }
  .brand {
    font-family: "Exo 2", sans-serif;
    font-weight: 800;
    color: var(--ink);
    display: flex;
    align-items: center;
    gap: 6px;
    letter-spacing: .2px;
  }
  .brand-dot { width: 12px; height: 12px; border-radius: 50%; background: var(--blue); }
  .brand--light { color: #fff; }
  .address { font-size: 6px; line-height: 1.45; color: var(--muted); text-align: right; }
  .stripe { position: absolute; left: 0; bottom: 14px; display: flex; flex-direction: column; }
  .stripe span { width: 8px; height: 12px; display: block; }
  .stripe .s1 { background: var(--grey); }
  .stripe .s2 { background: var(--green); }
  .stripe .s3 { background: var(--blue); }
  .stripe .s4 { background: var(--orange); }

  .letterhead { left: 430px; top: 30px; width: 300px; height: 410px; padding: 18px; }
  .letterhead .brand { font-size: 15px; }
  .letterhead .address { position: absolute; right: 18px; top: 20px; }

  .slip { left: 50px; top: 250px; width: 320px; height: 180px; padding: 16px; }
  .slip .brand { font-size: 14px; }
  .slip .address { text-align: left; margin-top: 6px; }

  .invoice { left: 780px; top: 150px; width: 320px; height: 330px; padding: 18px; }
  .invoice .brand { font-size: 15px; }
  .invoice .address { position: absolute; right: 18px; top: 20px; }
  .invoice-title { position: absolute; right: 18px; top: 110px; font-weight: 800; font-size: 13px; }
  .invoice-table { position: absolute; left: 18px; right: 18px; top: 130px; border-collapse: collapse; font-size: 7px; }
  .invoice-table th { text-align: left; font-weight: 600; border: 1px solid #555; padding: 3px; }
  .invoice-table td { border: 1px solid #555; height: 14px; }

  .envelope { left: 880px; top: 470px; width: 280px; height: 150px; overflow: hidden; }
  .envelope svg { position: absolute; left: 0; top: 0; }
  .envelope .brand-dot { position: absolute; left: 132px; top: 48px; width: 16px; height: 16px; }

  .card { position: absolute; width: 240px; height: 150px; background: var(--black); border-radius: 8px; box-shadow: 0 6px 18px rgba(0,0,0,.5); color: #fff; overflow: hidden; }
  .card-front { left: 380px; top: 540px; padding: 18px; }
  .card-front .brand { font-size: 22px; margin-top: 30px; }
  .card-front .web { position: absolute; left: 18px; bottom: 16px; font-size: 8px; color: #ccc; }
  .card-back { left: 640px; top: 540px; padding: 16px; }
  .card-back .brand { font-size: 13px; }
  .person { position: absolute; right: 16px; top: 50px; text-align: right; }
  .person-name { font-size: 12px; font-weight: 600; color: var(--orange); }
  .person-role { font-size: 7px; color: #ccc; margin-bottom: 6px; }
  .person-contact { font-size: 6.5px; line-height: 1.5; color: #ddd; }
  .card .stripe { bottom: 18px; }
</style>
</head>
<body>

  <section class="sheet letterhead">
    <div class="brand"><span class="brand-dot"></span>TheByteDepot</div>
    <div class="address">Birch Court<br>7X Fernhill Street<br>Harrow, London<br>HBX 8QW<br>0208 731 XXXX</div>
    <div class="stripe"><span class="s1"></span><span class="s2"></span><span class="s3"></span><span class="s4"></span></div>
  </section>

  <section class="sheet slip">
    <div class="brand"><span class="brand-dot"></span>TheByteDepot</div>
    <div class="address">Birch Court, 7X Fernhill Street<br>Harrow, London HBX 8QW</div>
    <div class="stripe"><span class="s1"></span><span class="s2"></span><span class="s3"></span><span class="s4"></span></div>
  </section>

  <section class="sheet invoice">
    <div class="brand"><span class="brand-dot"></span>TheByteDepot</div>
    <div class="address">Birch Court<br>7X Fernhill Street<br>Harrow, London<br>HBX 8QW</div>
    <div class="invoice-title">FAX</div>
    <table class="invoice-table">
      <tr><th>To</th><th>From</th><th>Date</th><th>Pages</th><th>Ref</th></tr>
      <tr><td></td><td></td><td></td><td></td><td></td></tr>
    </table>
    <div class="stripe"><span class="s1"></span><span class="s2"></span><span class="s3"></span><span class="s4"></span></div>
  </section>

  <section class="sheet envelope">
    <svg width="280" height="150" viewBox="0 0 280 150" aria-hidden="true">
      <path d="M0 0 H280 V40 Q140 110 0 40 Z" fill="var(--black)"/>
    </svg>
    <span class="brand-dot"></span>
  </section>

  <section class="card card-front">
    <div class="brand brand--light"><span class="brand-dot"></span>TheByteDepot</div>
    <div class="web">thebytedepotz.com</div>
  </section>

  <section class="card card-back">
    <div class="brand brand--light"><span class="brand-dot"></span>TheByteDepot</div>
    <div class="person">
      <div class="person-name">Pavel Orsk</div>
      <div class="person-role">Sales &amp; Logistics</div>
      <div class="person-contact">
        0208 731 XXXX<br>07452168XXX<br>pavel@thebytedepotz.com<br>thebytedepotz.com
      </div>
    </div>
    <div class="stripe"><span class="s1"></span><span class="s2"></span><span class="s3"></span><span class="s4"></span></div>
  </section>

</body>
</html>
```